Blue Ladle Handcrafted Tomato Ketchup packaging design modern

From the best ingredients there is the best ketchup Blue Handcrafted ketchup are specially formulated for fine dining and drinks, bringing out all the flavors. As the Blue Ladle handcrafted ketchup is otherwise fabulous: Made with wholesome, fully ripe fruits Nothing with half things! All Blue Ladle handcrafted ketchups are pure nature, without any artificial diluents or concentrates. Where tomato is on it, that's all there is to it - guaranteed! the design should be professional and noble despite being trendy. A watcher wants to sell the ketchup as merchandising from our restaurant. but as a single brand positioning. The ketchup is vegan. Dimensions: 6.8 cm Height: 7.8 cm Circumference: 21.6 cm The text down (Text 1-4). The lid of the text the glass packaging is black! Thanks for your efforts. I look forward to your designs.

Target Market(s)

foodies

Font styles to use
Serif
Sans Serif

Colors

Designer to choose colors to be used in the design.

Requirements
Must have
• Title: (Handcrafted Tomato Ketchup) Text One: (Store chilled after opening and consume quickly, pasteurized.) Text Two: (Handcrafted in Switzerland by Brennwald Kulinarik GmbH, Chur www.blueladle-sample.ch) Text Tree: (Tomatoes, White Wine Vinegar, Aceto Balsamico, Brown Cane Sugar, Corn Starch, Spices, Salt) Text For: (200 grams) or (200g) The Logo of Blue Ladle with the Pasta and Wine have to because of the gesety.
Nice to have
• small vegan icon (maybe)
Should not have
• text of the logo (pasta & wine)

```html
<!DOCTYPE html>
<html lang="de">
<head>
<meta charset="utf-8">
<title>Blue Ladle Tomato Ketchup – Etikett</title>
<link href="https://fonts.googleapis.com/css2?family=Bebas+Neue&family=Oswald:wght@300;400&family=Montserrat:wght@500&display=swap" rel="stylesheet">
<style>
  :root {
    --canvas: #ffffff;
    --label: #eef0ef;
    --ink: #1c1c1c;
    --ink-soft: #2e2e2e;
    --muted: #5a5a5a;
    --edge: #d9dcdb;
  }
  * { margin: 0; padding: 0; box-sizing: border-box; }
  html, body {
    width: 1200px; height: 1200px; overflow: hidden;
    background: var(--canvas);
  }
  .canvas { position: relative; width: 1200px; height: 1200px; }

  .label {
    position: absolute; left: 60px; top: 435px;
    width: 1080px; height: 330px;
    background: var(--label);
    border: 1px solid var(--edge);
    display: flex;
  }
  .panel { position: relative; width: 50%; height: 100%; }

  /* front panel */
  .product-title {
    position: absolute; left: 60px; top: 70px;
    font-family: "Bebas Neue", sans-serif; font-weight: 400;
    color: var(--ink);
  }
  .product-title .variety {
    display: block;
    font-size: 42px; line-height: 44px; letter-spacing: 8px;
  }
  .product-title .product {
    display: block;
    font-size: 120px; line-height: 110px; letter-spacing: 1px;
  }
  .brand-name {
    position: absolute; left: 62px; top: 262px;
    font-family: "Montserrat", sans-serif; font-weight: 500;
    font-size: 19px; letter-spacing: 5px;
    color: var(--ink);
  }

  /* back panel */
  .info-block {
    position: absolute; left: 200px;
    border-left: 4px solid var(--ink);
    padding-left: 12px;
    font-family: "Oswald", sans-serif; font-weight: 300;
    font-size: 11.5px; line-height: 15px;
    text-transform: uppercase; color: var(--muted);
    width: 200px;
  }
  .info-ingredients { top: 40px; }
  .info-storage { top: 96px; }
  .info-maker { top: 190px; height: 112px; }
  .info-maker .web { margin-top: 22px; }
  .info-maker .weight {
    margin-top: 26px; font-weight: 400; font-size: 13px; color: var(--ink-soft);
  }
</style>
</head>
<body>
<main class="canvas">
  <section class="label" aria-label="Etikett Blue Ladle Tomato Ketchup">
    <div class="panel panel-front">
      <h1 class="product-title">
        <span class="variety">Tomato</span>
        <span class="product">Ketchup</span>
      </h1>
      <p class="brand-name">BLUE LADLE</p>
    </div>
    <div class="panel panel-back">
      <p class="info-block info-ingredients">Tomaten, Weissweinessig, Aceto Balsamico, Brauner Rohrzucker, Maisstärke, Gewürze, Salz</p>
      <p class="info-block info-storage">Nach dem Öffnen gekühlt aufbewahren und rasch konsumieren. Pasteurisiert.</p>
      <div class="info-block info-maker">
        <p>Handcrafted in Switzerland<br>by Brennwald Kulinarik GmbH, Chur</p>
        <p class="web">www.blueladle-sample.ch</p>
        <p class="weight">200 Gramm</p>
      </div>
    </div>
  </section>
</main>
</body>
</html>
```